KRIVO is a 8-minute, fast-acting, chewable form of Lomexa

Description of Product Packaging
The name KRIVO was specifically chosen because it describes the sound of sex and has the word 'hump' in the name. The KRIVO logo is the actual letters, cracking the ground with such force that it shatters the foundation. The sides of the letters are pulsating to mimick the pulsating male genitalia. The marketing for KRIVO should be geared towards male consumers -- specfically, younger men who will use this product for recreational purposes.

1) The word Krivo needs to be on each side of the box
2) Remove all pictures and focus on the product not the people
3) Main Focus should eye catching.

I would like you to design the packaging for the following receptacles:
1) Sample pack (contains 1 pill)
2) Standard box (contains one 10-pill blister pack)
3) Bottle / Box (contains 20 pills)
4) Bottle / Box (contains 50 pills)
5) Bottle / Box (contains 100 pills)
ANY HELPFUL CONTENT YOU WANT

Target Market(s)

Men 18 to 100

Industry/Entity Type

Product

Requirements
Must have
• Please incorporate the logo on each side/panel of the packaging.
• Please make sure the design includes spaces for the barcode and the dosage information.
• Slick, cool young focus design.
• No to sexual to cause embarrassment to buy.
Nice to have
• Since KRIVO is a double-entendre, the tagline and copywriting should have a sense of playfulness and a sense of humor.
Should not have
• I do not want erotic images of couples on the packaging. Other images are acceptable as long as they are not lewd in nature.

```html
<!DOCTYPE html>
<html lang="en">
<head>
<meta charset="utf-8">
<title>KRIVO Chewable Tablets – Blister Box Dieline</title>
<link rel="stylesheet" href="https://fonts.googleapis.com/css2?family=Oswald:wght@400;500;700&family=Noto+Serif:wght@400;700&family=Archivo+Black&family=Roboto:wght@400;500&display=swap">
<style>
  :root {
    --red: #e3121b;
    --deep-red: #b00d14;
    --ink: #1b1b1b;
    --panel-dark: #2a2a2a;
    --cut-line: #9a9a9a;
    --paper: #ffffff;
    --page: #ffffff;
  }
  html, body {
    margin: 0;
    padding: 0;
    width: 800px;
    height: 1200px;
    overflow: hidden;
    background: var(--page);
  }
  .canvas {
    position: relative;
    width: 800px;
    height: 1200px;
  }
  .dieline {
    position: absolute;
    left: 0;
    top: 188px;
    width: 800px;
    height: 823px;
  }
  .cut { fill: var(--paper); stroke: var(--cut-line); stroke-width: 1; }
  .panel-edge { fill: none; stroke: var(--cut-line); stroke-width: 1; }
  .brand { font-family: 'Oswald', sans-serif; font-weight: 700; fill: var(--ink); letter-spacing: 1px; }
  .label { font-family: 'Oswald', sans-serif; font-weight: 500; fill: var(--ink); }
  .label-light { font-family: 'Oswald', sans-serif; font-weight: 400; fill: #ffffff; }
  .spaced { font-family: 'Archivo Black', sans-serif; fill: var(--ink); letter-spacing: 3px; }
  .heavy { font-family: 'Archivo Black', sans-serif; fill: var(--ink); }
  .serif { font-family: 'Noto Serif', serif; fill: var(--ink); }
  .serif-light { font-family: 'Noto Serif', serif; fill: #ffffff; }
  .serif-red { font-family: 'Noto Serif', serif; font-weight: 700; fill: var(--deep-red); }
  .claim-number { font-family: 'Roboto', sans-serif; font-weight: 400; fill: none; stroke: #ffffff; stroke-width: 5; }
  .claim-word { font-family: 'Roboto', sans-serif; font-weight: 500; fill: var(--red); }
  .claim-sub { font-family: 'Archivo Black', sans-serif; fill: var(--red); }
  .count-number { font-family: 'Oswald', sans-serif; font-weight: 500; fill: #ffffff; }
  .count-word { font-family: 'Oswald', sans-serif; font-weight: 400; fill: #ffffff; }
  .pill-tag { fill: var(--ink); }
  .dark-bar { fill: var(--panel-dark); }
  .red-bar { fill: var(--red); }
  .field { fill: #ffffff; }
  .barcode-space { fill: #ffffff; stroke: #bdbdbd; stroke-width: 1; }
</style>
</head>
<body>
<div class="canvas">
<svg class="dieline" viewBox="60 578 880 905" xmlns="http://www.w3.org/2000/svg">
  <defs>
    <linearGradient id="front-bg" x1="0" y1="0" x2="1" y2="0">
      <stop offset="0" stop-color="#a9a9a9"/>
      <stop offset="0.35" stop-color="#f4f4f4"/>
      <stop offset="0.6" stop-color="#ffe3e3"/>
      <stop offset="1" stop-color="#e3121b"/>
    </linearGradient>
    <linearGradient id="front-shade" x1="0" y1="0" x2="0" y2="1">
      <stop offset="0" stop-color="#000" stop-opacity="0.25"/>
      <stop offset="0.45" stop-color="#000" stop-opacity="0"/>
    </linearGradient>
    <linearGradient id="flap-bg" x1="0" y1="1" x2="0" y2="0">
      <stop offset="0" stop-color="#8f8f8f"/>
      <stop offset="1" stop-color="#ffffff"/>
    </linearGradient>
    <linearGradient id="side-left-bg" x1="1" y1="0" x2="0" y2="1">
      <stop offset="0" stop-color="#6d6d6d"/>
      <stop offset="0.5" stop-color="#f2f2f2"/>
      <stop offset="1" stop-color="#ffffff"/>
    </linearGradient>
    <linearGradient id="side-right-bg" x1="0" y1="0" x2="1" y2="0">
      <stop offset="0" stop-color="#ffe0e0"/>
      <stop offset="1" stop-color="#e3121b"/>
    </linearGradient>
    <linearGradient id="bottom-bg" x1="0" y1="0" x2="1" y2="0">
      <stop offset="0" stop-color="#e3121b"/>
      <stop offset="0.3" stop-color="#ffffff"/>
      <stop offset="0.55" stop-color="#ffffff"/>
      <stop offset="1" stop-color="#e3121b"/>
    </linearGradient>
    <linearGradient id="back-bg" x1="0" y1="0" x2="1" y2="0">
      <stop offset="0" stop-color="#ffffff"/>
      <stop offset="0.7" stop-color="#ffffff"/>
      <stop offset="1" stop-color="#e3121b"/>
    </linearGradient>
    <linearGradient id="claim-bg" x1="0" y1="0" x2="1" y2="0">
      <stop offset="0" stop-color="#e3121b"/>
      <stop offset="0.35" stop-color="#e3121b"/>
      <stop offset="0.45" stop-color="#d9d9d9"/>
      <stop offset="1" stop-color="#9d9d9d"/>
    </linearGradient>
    <linearGradient id="count-bg" x1="0" y1="0" x2="1" y2="0">
      <stop offset="0" stop-color="#1b1b1b"/>
      <stop offset="1" stop-color="#4a4a4a"/>
    </linearGradient>
    <radialGradient id="figure-tone" cx="0.5" cy="0.5" r="0.5">
      <stop offset="0" stop-color="#f08a8a" stop-opacity="0.45"/>
      <stop offset="1" stop-color="#f08a8a" stop-opacity="0"/>
    </radialGradient>
  </defs>

  <!-- ===== Tuck flaps and glue flaps ===== -->
  <g class="flaps">
    <path class="cut" d="M240 605 L160 605 Q150 605 150 615 L150 680 L240 692 Z"/>
    <path class="cut" d="M762 605 L840 605 Q850 605 850 615 L850 680 L762 692 Z"/>
    <path class="cut" d="M135 692 L90 692 Q70 692 70 712 L70 983 Q70 1003 90 1003 L135 1003 Z"/>
    <path class="cut" d="M865 692 L910 692 Q930 692 930 712 L930 983 Q930 1003 910 1003 L865 1003 Z"/>
    <path class="cut" d="M240 1015 L160 1015 Q150 1015 150 1025 L150 1090 L240 1095 Z"/>
    <path class="cut" d="M762 1015 L840 1015 Q850 1015 850 1025 L850 1090 L762 1095 Z"/>
    <path class="cut" d="M240 1410 L240 1458 Q240 1468 250 1468 L752 1468 Q762 1468 762 1458 L762 1410 Z"/>
  </g>

  <!-- ===== Top end panel (printed upside down) ===== -->
  <g class="panel-top" transform="rotate(180 501 641)">
    <rect x="240" y="590" width="522" height="102" fill="url(#flap-bg)"/>
    <text class="brand" x="266" y="655" font-size="34">KRIVO</text>
    <text class="spaced" x="368" y="630" font-size="11">TABLETS</text>
    <text class="spaced" x="368" y="645" font-size="11">CHEWABLE</text>
    <rect class="pill-tag" x="598" y="620" width="140" height="22" rx="5"/>
    <text class="serif-light" x="668" y="636" font-size="14" text-anchor="middle">100mg Sildenafil</text>
    <text class="serif" x="668" y="663" font-size="14" text-anchor="middle">Sildenafil Citrate</text>
  </g>
  <rect class="panel-edge" x="240" y="590" width="522" height="102"/>

  <!-- ===== Left side panel ===== -->
  <rect x="135" y="692" width="105" height="311" fill="url(#side-left-bg)"/>
  <g class="panel-left" transform="translate(240 692) rotate(90)">
    <text class="brand" x="18" y="38" font-size="32">KRIVO</text>
    <text class="spaced" x="110" y="50" font-size="10">CHEWABLE</text>
    <text class="spaced" x="110" y="63" font-size="10">TABLETS</text>
    <rect class="pill-tag" x="205" y="22" width="100" height="14" rx="4"/>
    <text class="serif-light" x="255" y="32" font-size="8" text-anchor="middle">100mg Sildenafil</text>
    <text class="serif" x="255" y="46" font-size="8" text-anchor="middle">Sildenafil Citrate</text>
    <rect x="205" y="62" width="106" height="30" fill="url(#count-bg)"/>
    <text class="count-number" x="212" y="87" font-size="26">10</text>
    <text class="count-word" x="244" y="85" font-size="15">TABLETS</text>
  </g>
  <rect class="panel-edge" x="135" y="692" width="105" height="311"/>

  <!-- ===== Right side panel ===== -->
  <rect x="762" y="692" width="103" height="311" fill="url(#side-right-bg)"/>
  <g class="panel-right" transform="translate(762 1003) rotate(-90)">
    <text class="brand" x="20" y="82" font-size="30">KRIVO</text>
    <text class="spaced" x="110" y="45" font-size="10">CHEWABLE</text>
    <text class="spaced" x="110" y="58" font-size="10">TABLETS</text>
    <rect class="pill-tag" x="215" y="16" width="88" height="14" rx="4"/>
    <text class="serif-light" x="259" y="26" font-size="7.5" text-anchor="middle">100mg Sildenafil</text>
    <text class="serif" x="259" y="40" font-size="7.5" text-anchor="middle">Sildenafil Citrate</text>
    <rect x="205" y="56" width="106" height="32" fill="url(#count-bg)"/>
    <text class="count-number" x="212" y="82" font-size="26">10</text>
    <text class="count-word" x="244" y="80" font-size="15">TABLETS</text>
  </g>
  <rect class="panel-edge" x="762" y="692" width="103" height="311"/>

  <!-- ===== Front panel ===== -->
  <g class="panel-front">
    <rect x="240" y="692" width="522" height="311" fill="url(#front-bg)"/>
    <rect x="240" y="692" width="522" height="311" fill="url(#front-shade)"/>
    <ellipse cx="610" cy="835" rx="100" ry="130" fill="url(#figure-tone)" role="img" aria-label="Decorative red line-art figure area"/>

    <text class="brand" x="298" y="812" font-size="56">KRIVO</text>

    <line x1="243" y1="857" x2="533" y2="857" stroke="var(--ink)" stroke-width="3"/>
    <rect class="pill-tag" x="250" y="863" width="160" height="27" rx="6"/>
    <text class="serif-light" x="330" y="882" font-size="17" text-anchor="middle">100mg Sildenafil</text>
    <text class="heavy" x="425" y="875" font-size="15">CHEWABLE</text>
    <text class="heavy" x="425" y="890" font-size="15">TABLETS</text>

    <rect x="230" y="900" width="252" height="86" rx="6" fill="url(#claim-bg)"/>
    <text class="claim-number" x="254" y="972" font-size="78">8</text>
    <text class="claim-word" x="324" y="950" font-size="42">Minute</text>
    <text class="claim-sub" x="326" y="970" font-size="17">Fast-Acting</text>

    <line x1="664" y1="899" x2="762" y2="899" stroke="var(--red)" stroke-width="2"/>
    <text class="serif" x="677" y="920" font-size="15">Sildenafil</text>
    <text class="serif" x="677" y="935" font-size="15">Citrate</text>

    <rect x="655" y="963" width="107" height="35" fill="url(#count-bg)"/>
    <text class="count-number" x="672" y="993" font-size="30">10</text>
    <text class="count-word" x="704" y="989" font-size="16">TABLETS</text>
  </g>
  <rect class="panel-edge" x="240" y="692" width="522" height="311"/>

  <!-- ===== Bottom end panel ===== -->
  <g class="panel-bottom">
    <rect x="240" y="1003" width="522" height="104" fill="url(#bottom-bg)"/>
    <text class="brand" x="266" y="1075" font-size="34">KRIVO</text>
    <text class="spaced" x="366" y="1060" font-size="12">CHEWABLE</text>
    <text class="spaced" x="366" y="1075" font-size="12">TABLETS</text>
    <rect class="pill-tag" x="608" y="1034" width="140" height="22" rx="5"/>
    <text class="serif-light" x="678" y="1050" font-size="15" text-anchor="middle">100mg Sildenafil</text>
    <text class="serif-red" x="678" y="1075" font-size="14" text-anchor="middle">Sildenafil Citrate</text>
  </g>
  <rect class="panel-edge" x="240" y="1003" width="522" height="104"/>

  <!-- ===== Back panel ===== -->
  <g class="panel-back">
    <rect x="240" y="1107" width="522" height="303" fill="url(#back-bg)"/>

    <g class="directions">
      <rect class="dark-bar" x="268" y="1128" width="190" height="17"/>
      <text class="label-light" x="292" y="1141" font-size="11">DIRECTIONS</text>
      <rect class="dark-bar" x="268" y="1151" width="190" height="17"/>
      <text class="label-light" x="292" y="1164" font-size="12">DOSAGE</text>
      <rect class="red-bar" x="268" y="1170" width="190" height="17"/>
      <text class="label-light" x="292" y="1183" font-size="10">AS DIRECTED BY THE PHYSICIAN</text>

      <rect class="dark-bar" x="268" y="1208" width="190" height="17"/>
      <text class="label-light" x="292" y="1221" font-size="12">STORAGE</text>
      <rect class="dark-bar" x="268" y="1227" width="190" height="35"/>
      <text class="label-light" x="292" y="1240" font-size="10">STORE IN A COOL DRY PLACE.</text>
      <text class="label-light" x="292" y="1257" font-size="10">PROTECT FROM LIGHT.</text>
      <rect class="red-bar" x="268" y="1263" width="190" height="16"/>
      <text class="label-light" x="292" y="1275" font-size="10">KEEP OUT OF REACH OF CHILDREN.</text>
    </g>

    <rect class="barcode-space" x="276" y="1296" width="118" height="94" role="img" aria-label="Barcode space"/>

    <g class="composition">
      <rect class="field" x="490" y="1127" width="257" height="83"/>
      <text class="label" x="497" y="1149" font-size="13">EACH UNCOATED TABLETS CONTAINS</text>
      <line x1="497" y1="1154" x2="747" y2="1154" stroke="var(--ink)" stroke-width="1"/>
      <text class="serif" x="497" y="1170" font-size="11.5" font-weight="700">SLIDENAFIL CITRATE equivalent to</text>
      <text class="serif" x="497" y="1186" font-size="11.5" font-weight="700">SLIDENAFIL</text>
      <text class="serif" x="742" y="1186" font-size="11.5" font-weight="700" text-anchor="end">100 mg</text>
      <text class="serif" x="497" y="1202" font-size="11.5" font-weight="700">APPOVED COLOR USED</text>

      <text class="label" x="495" y="1232" font-size="13">MFG DATE</text>
      <rect class="field" x="552" y="1219" width="195" height="15" stroke="#dddddd"/>
      <text class="label" x="495" y="1254" font-size="13">EXP DATE</text>
      <rect class="field" x="552" y="1241" width="195" height="15" stroke="#dddddd"/>
    </g>

    <g class="maker">
      <text class="label" x="657" y="1296" font-size="8" text-anchor="end">MANUFACTURED BY</text>
      <text class="label" x="657" y="1318" font-size="19" text-anchor="end">KRIVO HEALTH CARE INC</text>
      <text class="brand" x="668" y="1330" font-size="28">KRIVO</text>
      <text class="heavy" x="494" y="1362" font-size="15">www.krivo-health.com</text>
    </g>

    <rect x="655" y="1377" width="107" height="33" fill="url(#count-bg)"/>
    <text class="count-number" x="672" y="1405" font-size="30">10</text>
    <text class="count-word" x="704" y="1401" font-size="16">TABLETS</text>
  </g>
  <rect class="panel-edge" x="240" y="1107" width="522" height="303"/>
</svg>
</div>
</body>
</html>
```